Banner Design for Physiotherapy Business

I need a banner designed for a physiotherapy business. The word ‘Physiotherapy’ should be prominent at the top. I’ve attached a document outlining what text and a suggestion of a picture I’d like included. The photo I have suggested in the document won’t upload to plumvista though as the dimensions are too large. I am open to other photos being used though. I would like to see designs that use the colour orange (as seen in the example) or green preferrably. The dimensions need to be 841mm x 2055mm and provided in PDF, JPG, and PNG format and 300dpi in CMYK colour mode.

```html
<!DOCTYPE html>
<html lang="en">
<head>
<meta charset="utf-8">
<title>Physiotherapy Roll-up Banner</title>
<link href="https://fonts.googleapis.com/css2?family=Oswald:wght@600&family=Montserrat:wght@300;600;700;800&display=swap" rel="stylesheet">
<style>
  :root {
    --page: #e6e7e3;
    --white: #ffffff;
    --orange: #f26a1b;
    --orange-deep: #e0420f;
    --orange-light: #ff8a2a;
    --ink: #141414;
    --badge: #1f7fc9;
    --photo-a: #f4f1ec;
    --photo-b: #d9d4cc;
  }
  * { box-sizing: border-box; margin: 0; padding: 0; }
  html, body { width: 1200px; height: 1200px; overflow: hidden; }
  body { background: var(--page); font-family: "Montserrat", sans-serif; color: var(--ink); }

  .banner {
    position: absolute; left: 365px; top: 26px;
    width: 470px; height: 1148px;
    background: var(--white);
    box-shadow: 0 6px 24px rgba(0,0,0,.12);
    overflow: hidden;
  }
  .title {
    position: absolute; left: 0; top: 24px; width: 100%;
    text-align: center; white-space: nowrap;
    font-family: "Oswald", sans-serif; font-weight: 600;
    font-size: 62px; line-height: 1; letter-spacing: -0.5px;
    color: var(--orange-deep);
    transform: scaleY(1.6); transform-origin: top center;
  }
  .hero { position: absolute; left: 0; top: 150px; width: 470px; height: 320px; }

  .services-heading { position: absolute; left: 40px; top: 455px; }
  .services-heading .lead { font-weight: 300; font-size: 25px; letter-spacing: .5px; line-height: 1; }
  .services-heading .main { font-weight: 800; font-size: 32px; color: var(--orange); line-height: 1.05; letter-spacing: -.5px; }

  .service-list { position: absolute; left: 40px; top: 528px; width: 410px; list-style: none; }
  .service-list li {
    display: flex; align-items: flex-start; gap: 10px;
    font-weight: 700; font-size: 15px; line-height: 19px;
    text-transform: uppercase; margin-bottom: 8.5px;
  }
  .service-list .num {
    flex: none; width: 22px; height: 22px; margin-top: -2px;
    border: 1.5px solid var(--orange-deep); border-right-color: transparent; border-radius: 50%;
    color: var(--orange-deep); font-size: 9px; font-weight: 700;
    display: flex; align-items: center; justify-content: center;
  }

  .member { position: absolute; left: 40px; top: 1040px; display: flex; align-items: center; gap: 10px; }
  .member .dot { width: 40px; height: 40px; border-radius: 50%; background: var(--badge); }
  .member .name { font-weight: 600; font-size: 12px; line-height: 1.25; color: var(--badge); text-transform: uppercase; }

  .appointment {
    position: absolute; right: 0; top: 1018px; width: 230px; height: 80px;
    background: linear-gradient(90deg, var(--orange) 0%, var(--orange-deep) 100%);
    border-radius: 6px 0 0 6px; padding: 10px 14px; color: var(--white);
  }
  .appointment h3 { font-weight: 800; font-size: 14px; letter-spacing: .2px; margin-bottom: 3px; }
  .appointment p { font-weight: 300; font-size: 10.5px; line-height: 1.3; }
</style>
</head>
<body>
  <main class="banner">
    <h1 class="title">PHYSIOTHERAPY</h1>

    <svg class="hero" viewBox="0 0 470 320" role="img" aria-label="Photo of a physiotherapist guiding an older man through a dumbbell shoulder exercise in a bright clinic">
      <defs>
        <linearGradient id="photoTone" x1="0" y1="0" x2="1" y2="1">
          <stop offset="0" stop-color="var(--photo-a)"/>
          <stop offset="1" stop-color="var(--photo-b)"/>
        </linearGradient>
      </defs>
      <rect x="0" y="0" width="470" height="7" fill="var(--orange-light)"/>
      <rect x="0" y="7" width="470" height="9" fill="var(--orange-deep)"/>
      <polygon points="0,16 470,16 470,300 340,300 288,268 0,268" fill="url(#photoTone)"/>
      <polyline points="0,273 286,273 338,305 470,305" fill="none" stroke="var(--orange-deep)" stroke-width="9"/>
      <polyline points="0,283 282,283 334,315 470,315" fill="none" stroke="var(--orange-light)" stroke-width="5"/>
    </svg>

    <div class="services-heading">
      <p class="lead">WHAT WE</p>
      <h2 class="main">TREAT / SERVICES</h2>
    </div>

    <ol class="service-list">
      <li><span class="num">1.</span>Arthritis</li>
      <li><span class="num">2.</span>Back pain / Neck pain</li>
      <li><span class="num">3.</span>Sciatic pain</li>
      <li><span class="num">4.</span>Sports injuries</li>
      <li><span class="num">5.</span>Repetitive strain injuries</li>
      <li><span class="num">6.</span><span>Post surgical management<br>(hip and knee arthroscopes,<br>joint replacement surgery)</span></li>
      <li><span class="num">7.</span>Shoulder pain and dysfunction</li>
      <li><span class="num">8.</span>Tennis elbow</li>
      <li><span class="num">9.</span>Postural pain</li>
      <li><span class="num">10.</span>Workplace injuries</li>
      <li><span class="num">11.</span>Motor vehicle accidents</li>
      <li><span class="num">12.</span>Women’s health issues</li>
      <li><span class="num">13.</span>Clinical exercise</li>
      <li><span class="num">14.</span><span>Pre-employment functional<br>assessments</span></li>
    </ol>

    <div class="member">
      <span class="dot"></span>
      <span class="name">Kinetic Physio<br>Guild Member</span>
    </div>

    <section class="appointment">
      <h3>MAKE AN APPOINTMENT</h3>
      <p>Ridgeway Family Practice<br>18-20 Alder St, Ridgeway VIC 3999<br>(03) 5550 1234</p>
    </section>
  </main>
</body>
</html>
```